Sleep/Snoring Business - Requires Website - Australia

We are seeking a simple to maintain website for our sleep business. The health care business provides diagnostic and treatment solutions for snoring, sleep disorders and other respiratory problems.

Ideally, colours to match the company logo (attached).

The page must be built using WORDPRESS.

Ideally site will have a home page outlining the business, with 5 sub pages - being "Diagnosis" "Treatment Options", "Prodcuts", "About Us", "Contact Us"

The site home page should include a large picture on the home page.

The "Treatment Options" and "Diagnosis" pages must include:
Allow for a few pictures with assocaited text, plus space for some embeded youtube videos.

"Prodcuts" page should have the ability to show 3-4 products across the page with text below.. that can include external URL to products

The "About Us" page must include:
1. a Map (google map) to identify the various locations. There are 6 in total.
2. A Section to describe our doctors/staff - allow for a picture and some text

The "Contact Us" page must include:
email form
telephone details

The overall design should have a clean and medical/safe feeling

Target Market(s)

People who snore and those with sleeping and respiratory disorders

Industry/Entity Type

Health Care

Coding

Coded - Design and coding required

Number of Pages Required

5+ page

Colors

Designer to choose colors to be used in the design.

Requirements
Must have
• The page must be built using WORDPRESS.
• Ideally site will have a home page outlining the business, with 5 sub pages - being "Diagnosis" "Treatment Options", "Prodcuts", "About Us", "Contact Us"
• The site home page should include a large picture on the home page.
• The "Treatment Options" and "Diagnosis" pages must include:
• Allow for a few pictures with assocaited text, plus space for some embeded youtube videos.
• "Prodcuts" page should have the ability to show 3-4 products across the page with text below.. that can include external URL to products
• The "About Us" page must include:
• 1. a Map (google map) to identify the various locations. There are 6 in total.
• 2. A Section to describe our doctors/staff - allow for a picture and some text
• The "Contact Us" page must include:
• email form
• telephone details
• Pictures must be licenced or free to use
Nice to have
• Home page pictures showing people sleeping well, snoring or fresh air (landscape) type transition pictures (at least 3).
Should not have
• Not to look cheap
• This is a high end healthcare business, so must look that way

```html
<!DOCTYPE html>
<html lang="en">
<head>
<meta charset="utf-8">
<title>Restwell Clinics – Sleep Disorder Specialists</title>
<link href="https://fonts.googleapis.com/css2?family=Lato:wght@400;700;900&family=Open+Sans:wght@400;600&display=swap" rel="stylesheet">
<style>
:root{
  --blue:#1f5fa3;
  --blue-dark:#184b82;
  --blue-band:#2a5f97;
  --text:#3a3a3a;
  --muted:#7a7a7a;
  --line:#dcdcdc;
  --bg:#ffffff;
}
*{box-sizing:border-box;margin:0;padding:0}
html,body{width:1200px;height:3188px;overflow:hidden;background:var(--bg)}
body{font-family:"Open Sans",Arial,sans-serif;color:var(--text);font-size:13px;line-height:1.6;position:relative}
.wrap{width:1000px;margin:0 auto;position:relative}
h2.section-title{font-family:"Lato",Arial,sans-serif;font-weight:900;font-size:28px;letter-spacing:.5px;text-align:center;color:#222;text-transform:uppercase}
.btn{display:inline-block;border:1px solid var(--blue);color:var(--blue);font-size:11px;font-weight:600;padding:6px 16px;border-radius:3px;text-transform:uppercase;background:#fff;white-space:nowrap}
.btn.light{border-color:#fff;color:#fff;background:transparent}
.btn.solid{background:var(--blue);color:#fff}

/* header */
.site-header{height:72px;display:flex;align-items:center;justify-content:space-between;padding:0 100px 0 20px}
.brand{font-family:"Lato",Arial,sans-serif;font-weight:900;font-size:32px;color:var(--blue);display:flex;align-items:center;gap:10px}
.brand .dot{width:14px;height:14px;border-radius:50%;background:var(--blue)}
.head-right{display:flex;flex-direction:column;align-items:flex-end;gap:8px}
.contacts{display:flex;gap:22px;font-size:12px;color:#444}
.contacts span{display:flex;align-items:center;gap:6px}
.contacts svg{width:16px;height:16px}
.nav{display:flex;gap:22px;font-family:"Lato",Arial,sans-serif;font-size:13px;font-weight:700;color:#333}
.nav .active{color:var(--blue)}

/* hero */
.hero{position:relative;height:470px;overflow:hidden}
.hero-photo{position:absolute;inset:0;background:
  linear-gradient(90deg,rgba(40,55,75,.55) 0%,rgba(40,55,75,.35) 40%,rgba(40,55,75,0) 70%),
  linear-gradient(120deg,#7d8a9c 0%,#b8b3ad 40%,#e7ddd2 65%,#f4eee7 80%,#aeb8c4 100%)}
.hero-text{position:absolute;left:100px;top:44px;color:#fff;width:580px}
.hero-text h1{font-family:"Lato",Arial,sans-serif;font-weight:900;font-size:38px;line-height:1.2;text-transform:uppercase;text-shadow:0 1px 3px rgba(0,0,0,.3)}
.hero-text p{font-size:14px;margin:12px 0 22px;width:520px;text-shadow:0 1px 2px rgba(0,0,0,.45)}
.dots{position:absolute;left:0;right:0;top:385px;display:flex;justify-content:center;gap:7px}
.dots i{width:10px;height:10px;border-radius:50%;border:1px solid #fff;display:block}
.dots i.on{background:#fff}
.wave{position:absolute;left:0;bottom:-2px;width:1200px;height:110px}

/* welcome */
.welcome{padding-top:110px;text-align:center}
.welcome p{width:760px;margin:28px auto 30px;color:var(--muted);font-size:12px}
.divider{height:1px;background:var(--line);width:1000px;margin:70px auto 0}

/* treatments */
.treatments{padding-top:62px}
.cards{display:flex;gap:40px;margin-top:42px}
.card{width:306px}
.card .ph{height:206px;border:1px solid var(--line)}
.card h3{font-family:"Lato",Arial,sans-serif;font-weight:900;font-size:17px;margin:26px 0 8px;color:#222;text-transform:uppercase}
.card p{color:var(--muted);font-size:12px;margin-bottom:16px}

/* diagnostic band */
.diagnostic{margin-top:70px;height:400px;background:linear-gradient(90deg,#7f94b6 0%,#98abc8 50%,#b3c1d8 100%);position:relative}
.diagnostic .wrap{display:flex;justify-content:space-between;padding-top:44px}
.diag-text{width:420px;color:#fff}
.diag-text h2{font-family:"Lato",Arial,sans-serif;font-weight:900;font-size:26px;text-transform:uppercase}
.diag-text > p{font-size:12px;margin:10px 0 18px}
.ticks{list-style:none;font-size:12px;margin-bottom:24px}
.ticks li{display:flex;gap:10px;align-items:center;margin-bottom:6px}
.ticks li:before{content:"";width:10px;height:10px;border-radius:50%;background:#fff;opacity:.85}
.video{width:500px;height:312px;background:#fff;border:3px solid #fff;position:relative}
.video-bar{height:30px;background:rgba(30,30,30,.85);color:#fff;font-size:12px;padding:6px 10px;position:absolute;top:0;left:0;right:0;z-index:2}
.video .ph{position:absolute;inset:0;background:linear-gradient(135deg,#9fd0e2 0%,#c6e4ee 35%,#f0c9d6 65%,#a9d6e4 100%)}
.play{position:absolute;left:50%;top:50%;width:56px;height:56px;margin:-28px 0 0 -28px;border-radius:50%;background:rgba(20,20,20,.85);z-index:2}
.play:after{content:"";position:absolute;left:22px;top:17px;border-left:16px solid #fff;border-top:11px solid transparent;border-bottom:11px solid transparent}

/* blog */
.blog{padding-top:80px}
.posts{display:flex;gap:60px;margin-top:42px}
.post{display:flex;gap:24px;width:470px}
.post .ph{width:220px;height:180px;flex:none}
.post h3{font-family:"Lato",Arial,sans-serif;font-weight:900;font-size:15px;text-transform:uppercase;color:#222}
.meta{font-size:11px;color:var(--muted);margin:6px 0}
.post p{font-size:12px;color:var(--muted);margin-bottom:14px}

/* testimonial */
.testimonial{margin-top:70px;height:210px;background:var(--blue-band);color:#fff;position:relative}
.testimonial .wrap{display:flex;gap:36px;padding:40px 90px 0}
.avatar{width:110px;height:110px;border-radius:50%;background:linear-gradient(#8fa6c0,#4f6b8c);border:3px solid #fff;flex:none}
.quote p{font-size:13px}
.quote .who{font-family:"Lato",Arial,sans-serif;font-weight:700;font-size:15px;margin-top:14px}
.arrow{position:absolute;top:90px;width:20px;height:30px}

/* contact */
.contact{padding-top:76px}
.contact-grid{display:flex;justify-content:space-between;margin-top:42px}
.form{width:620px}
.form h4,.info h4{font-family:"Lato",Arial,sans-serif;font-size:15px;font-weight:700;margin-bottom:16px;color:#222}
.row{display:flex;gap:16px;margin-bottom:12px}
.field{flex:1;height:32px;border:1px solid var(--line);font-size:11px;color:#999;padding:7px 10px}
.field.msg{height:90px}
.submit{display:flex;justify-content:flex-end;margin-top:10px}
.info{width:300px;border-left:1px solid var(--line);padding-left:30px}
.info li{list-style:none;display:flex;gap:12px;font-size:12px;color:var(--muted);margin-bottom:12px;align-items:flex-start}
.info li svg{width:16px;height:16px;flex:none;margin-top:2px}
.social{display:flex;gap:8px;margin-top:8px}
.social i{width:28px;height:28px;border-radius:50%;display:block}
.site-footer{position:absolute;left:0;right:0;bottom:0;height:52px;border-top:1px solid var(--line);text-align:center;font-size:11px;color:var(--muted);padding-top:18px}
</style>
</head>
<body>

<header class="site-header">
  <div class="brand"><span class="dot"></span>Restwell</div>
  <div class="head-right">
    <div class="contacts">
      <span><svg viewBox="0 0 16 16"><circle cx="8" cy="8" r="8" fill="#1f5fa3"/><path d="M5 4.5l2 2-1 1c.5 1 1.5 2 2.5 2.5l1-1 2 2-1 1.5C7.5 12 4 8.5 3.5 5.5z" fill="#fff"/></svg>1-800-555-0142</span>
      <span><svg viewBox="0 0 16 16"><circle cx="8" cy="8" r="8" fill="#1f5fa3"/><rect x="4" y="5" width="8" height="6" fill="#fff"/><path d="M4 5l4 3 4-3" stroke="#1f5fa3" fill="none"/></svg>info@restwellclinics.com</span>
    </div>
    <nav class="nav"><span class="active">Home</span><span>Diagnosis</span><span>Treatment Options</span><span>About us</span><span>Contact us</span></nav>
  </div>
</header>

<section class="hero">
  <div class="hero-photo" role="img" aria-label="Photo of a woman sleeping peacefully in a bright bedroom"></div>
  <div class="hero-text">
    <h1>Australia's Premier<br>Sleep Disorder Specialists</h1>
    <p>We provide diagnostic and treatment solutions for snoring, sleep disorders and other respiratory problems.</p>
    <span class="btn light">Schedule an appointment</span>
  </div>
  <div class="dots"><i class="on"></i><i></i><i></i><i></i></div>
  <svg class="wave" viewBox="0 0 1200 110" preserveAspectRatio="none">
    <path d="M0 110 L0 70 C300 10 700 120 1200 20 L1200 110 Z" fill="#fff"/>
    <path d="M0 70 C300 10 700 120 1200 20" stroke="#1f5fa3" stroke-width="5" fill="none"/>
    <path d="M0 82 C300 22 700 130 1200 34" stroke="#cfdcec" stroke-width="3" fill="none"/>
  </svg>
</section>

<section class="welcome wrap">
  <h2 class="section-title">Welcome to Restwell Clinics</h2>
  <p>Our team brings together sleep physicians, respiratory experts and caring staff to help you breathe easier and rest better. From your first assessment to ongoing treatment, we guide every step with clear advice, modern diagnostic tools and plans shaped around your health, your routine and your goals for a better night.</p>
  <span class="btn">About us</span>
</section>
<div class="divider"></div>

<section class="treatments wrap">
  <h2 class="section-title">Treatment Options For</h2>
  <div class="cards">
    <article class="card">
      <div class="ph" role="img" aria-label="Photo of a couple in bed, one partner snoring" style="background:linear-gradient(135deg,#f3ede6 0%,#d9c9b8 50%,#b9a690 100%)"></div>
      <h3>Snoring</h3>
      <p>Snoring can disturb your rest and your partner's sleep. We find the cause and offer proven options to quiet the night.</p>
      <span class="btn">Read more »</span>
    </article>
    <article class="card">
      <div class="ph" role="img" aria-label="Photo of a woman lying awake on a white pillow" style="background:linear-gradient(135deg,#ffffff 0%,#ede5dc 45%,#c7b19a 100%)"></div>
      <h3>Sleep Disorders</h3>
      <p>Insomnia, sleep apnoea and restless nights are assessed by specialists who tailor treatment to your needs.</p>
      <span class="btn">Read more »</span>
    </article>
    <article class="card">
      <div class="ph" role="img" aria-label="Photo of a tired man in bed beside a bedside clock" style="background:linear-gradient(135deg,#c9d3de 0%,#6f8197 50%,#2f3d50 100%)"></div>
      <h3>Other Respiratory Problems</h3>
      <p>Breathing problems at night affect daytime energy. Our clinicians review your airway and lung health with care.</p>
      <span class="btn">Read more »</span>
    </article>
  </div>
</section>

<section class="diagnostic" aria-label="Diagnostic techniques">
  <div class="wrap">
    <div class="diag-text">
      <h2>Diagnostic Techniques</h2>
      <p>We use reliable home and in-clinic sleep studies to understand how you breathe and rest through the night.</p>
      <ul class="ticks">
        <li>Overnight sleep studies in a calm setting</li>
        <li>Simple home testing with easy devices</li>
        <li>Airway and breathing assessment</li>
        <li>Clear results explained by our doctors</li>
      </ul>
      <span class="btn light">Read more</span>
    </div>
    <div class="video">
      <div class="video-bar">Diagnostic Techniques</div>
      <div class="ph" role="img" aria-label="Video still of an illustrated woman asleep in bed"></div>
      <div class="play"></div>
    </div>
  </div>
</section>

<section class="blog wrap">
  <h2 class="section-title">Latest Blog</h2>
  <div class="posts">
    <article class="post">
      <div class="ph" role="img" aria-label="Photo of a doctor speaking with a patient" style="background:linear-gradient(135deg,#eef3f8 0%,#a9c1d9 50%,#5f83a8 100%)"></div>
      <div>
        <h3>Finibus bonorum et malorum</h3>
        <div class="meta">08/03/2015 &nbsp;|&nbsp; Clinic team</div>
        <p>Simple habits that support deeper sleep and easier breathing, from bedtime routines to room setup.</p>
        <span class="btn">Read more »</span>
      </div>
    </article>
    <article class="post">
      <div class="ph" role="img" aria-label="Photo of a senior patient with a clinician" style="background:linear-gradient(135deg,#f5f1ec 0%,#d6c6b5 50%,#9aa7b5 100%)"></div>
      <div>
        <h3>Finibus bonorum et malorum</h3>
        <div class="meta">08/03/2015 &nbsp;|&nbsp; Clinic team</div>
        <p>What to expect during a sleep study and how our team uses the results to plan your care.</p>
        <span class="btn">Read more »</span>
      </div>
    </article>
  </div>
</section>

<section class="testimonial">
  <svg class="arrow" style="left:40px" viewBox="0 0 20 30"><path d="M16 3L4 15l12 12" stroke="#fff" stroke-width="3" fill="none"/></svg>
  <svg class="arrow" style="right:40px" viewBox="0 0 20 30"><path d="M4 3l12 12L4 27" stroke="#fff" stroke-width="3" fill="none"/></svg>
  <div class="wrap">
    <div class="avatar" role="img" aria-label="Portrait photo of the patient quoted"></div>
    <div class="quote">
      <p>After years of restless nights, the team found the cause of my snoring within weeks. The staff were patient, the tests were simple and every result was explained clearly. I now wake up rested and full of energy, and my family sleeps better too. I recommend the clinic to anyone who struggles with sleep.</p>
      <div class="who">- Martin Delcourt</div>
    </div>
  </div>
</section>

<section class="contact wrap">
  <h2 class="section-title">Contact Us</h2>
  <div class="contact-grid">
    <div class="form">
      <h4>Get in touch</h4>
      <div class="row"><div class="field">Name</div><div class="field">Phone no</div></div>
      <div class="row"><div class="field">Email</div></div>
      <div class="row"><div class="field msg">Message</div></div>
      <div class="submit"><span class="btn solid">Submit</span></div>
    </div>
    <div class="info">
      <h4>Contact Information</h4>
      <ul>
        <li><svg viewBox="0 0 16 16"><path d="M8 1a5 5 0 015 5c0 4-5 9-5 9S3 10 3 6a5 5 0 015-5z" fill="#888"/><circle cx="8" cy="6" r="2" fill="#fff"/></svg>12 Harbour Lane, Suite 4<br>Northbridge NSW 2000</li>
        <li><svg viewBox="0 0 16 16"><path d="M3 2l3 3-1.5 1.5c1 2 3 4 5 5L11 10l3 3-2 2C7 14 2 9 1 4z" fill="#888"/></svg>1-800-555-0142</li>
        <li><svg viewBox="0 0 16 16"><rect x="1" y="3" width="14" height="10" fill="#888"/><path d="M1 3l7 5 7-5" stroke="#fff" fill="none"/></svg>info@restwellclinics.com</li>
      </ul>
      <div class="social"><i style="background:#3b5998"></i><i style="background:#1da1f2"></i><i style="background:#dd4b39"></i><i style="background:#cb2027"></i></div>
    </div>
  </div>
</section>

<footer class="site-footer">Copyright © 2015 Restwell Clinics. All Rights Reserved.</footer>

</body>
</html>
```